Business Consulting Company needs a business card designed

We need a business card in Brisbane Australia for a company called " Brindlewood Consulting Group". I would like to see the designs either in purple or green color

```html
<!DOCTYPE html>
<html lang="en">
<head>
<meta charset="utf-8">
<title>Brindlewood Consulting Group – Business Card</title>
<link rel="stylesheet" href="https://fonts.googleapis.com/css2?family=Saira:wght@400&family=Open+Sans:wght@400;600&display=swap">
<style>
  :root {
    --backdrop: #a8a8a8;
    --card-white: #ffffff;
    --card-dark: #1d2023;
    --card-dark-edge: #131517;
    --brand-green: #1f9a52;
    --band-green: #4bb65a;
    --band-green-dark: #16954c;
    --text-black: #151515;
    --text-white: #ffffff;
  }
  * { box-sizing: border-box; margin: 0; padding: 0; }
  html, body {
    width: 1200px; height: 900px; overflow: hidden;
    background: var(--backdrop);
  }
  .card {
    position: absolute; left: 150px; top: 150px;
    width: 900px; height: 600px;
    border-radius: 36px; overflow: hidden;
    background: var(--card-white);
    box-shadow: 0 10px 30px rgba(0,0,0,0.25);
  }
  .card__header {
    position: absolute; left: 0; top: 0; width: 100%; height: 280px;
    background: var(--card-white);
  }
  .brand {
    position: absolute; left: 56px; top: 58px;
    display: flex; align-items: center; gap: 26px;
  }
  .brand__mark {
    width: 170px; height: 170px; border-radius: 50%;
    background: var(--brand-green);
    flex: none;
  }
  .brand__name {
    font-family: "Saira", "Open Sans", sans-serif;
    font-weight: 400; font-size: 41px; letter-spacing: 0.5px;
    color: var(--text-black); white-space: nowrap;
  }
  .card__band {
    position: absolute; left: 0; top: 280px; width: 100%; height: 18px;
    background: linear-gradient(to bottom, var(--band-green-dark) 0 4px, var(--band-green) 4px 100%);
  }
  .card__body {
    position: absolute; left: 0; top: 298px; width: 100%; height: 302px;
    background: linear-gradient(to bottom, var(--card-dark), var(--card-dark-edge));
    padding: 26px 60px 0;
    font-family: "Open Sans", sans-serif;
    color: var(--text-white);
  }
  .person__name {
    font-weight: 600; font-size: 34px; line-height: 1.15;
    color: var(--brand-green);
  }
  .person__role {
    font-size: 22px; line-height: 1.4; margin-bottom: 18px;
  }
  .contact { list-style: none; }
  .contact__item {
    display: flex; align-items: flex-start; gap: 10px;
    font-size: 24px; line-height: 32px;
  }
  .contact__icon { width: 26px; height: 26px; flex: none; margin-top: 4px; }
  .contact__icon * { fill: var(--brand-green); }
  .contact__address-line { display: block; padding-left: 10px; }
</style>
</head>
<body>
  <main class="card">
    <header class="card__header">
      <div class="brand">
        <span class="brand__mark"></span>
        <span class="brand__name">Brindlewood Consulting Group</span>
      </div>
    </header>
    <div class="card__band"></div>
    <section class="card__body">
      <h1 class="person__name">Mara Ellison</h1>
      <p class="person__role">manager</p>
      <ul class="contact">
        <li class="contact__item">
          <svg class="contact__icon" viewBox="0 0 24 24" aria-hidden="true"><path d="M6.6 10.8a15 15 0 0 0 6.6 6.6l2.2-2.2c.3-.3.7-.4 1-.2 1.1.4 2.3.6 3.6.6.6 0 1 .4 1 1V20c0 .6-.4 1-1 1C10.6 21 3 13.4 3 4c0-.6.4-1 1-1h3.5c.6 0 1 .4 1 1 0 1.3.2 2.5.6 3.6.1.3 0 .7-.2 1z"/></svg>
          <span>154-555-0172</span>
        </li>
        <li class="contact__item">
          <svg class="contact__icon" viewBox="0 0 24 24" aria-hidden="true"><path d="M12 2a10 10 0 1 0 0 20 10 10 0 0 0 0-20zm6.9 6h-2.9a15.7 15.7 0 0 0-1.4-3.6A8 8 0 0 1 18.9 8zM12 4c.8 1.2 1.5 2.5 1.9 4h-3.8c.4-1.5 1.1-2.8 1.9-4zM4.3 14a8 8 0 0 1 0-4h3.4a16 16 0 0 0 0 4zm.8 2h2.9c.3 1.3.8 2.5 1.4 3.6A8 8 0 0 1 5.1 16zM8 8H5.1a8 8 0 0 1 4.3-3.6C8.8 5.5 8.3 6.7 8 8zm4 12c-.8-1.2-1.5-2.5-1.9-4h3.8c-.4 1.5-1.1 2.8-1.9 4zm2.3-6H9.7a14 14 0 0 1 0-4h4.6a14 14 0 0 1 0 4zm.3 5.6c.6-1.1 1.1-2.3 1.4-3.6h2.9a8 8 0 0 1-4.3 3.6zm1.7-5.6a16 16 0 0 0 0-4h3.4a8 8 0 0 1 0 4z"/></svg>
          <span>www.brindlewoodgroup.com</span>
        </li>
        <li class="contact__item">
          <svg class="contact__icon" viewBox="0 0 24 24" aria-hidden="true"><path d="M2 6h20v13H2zm2 2v.4l8 5 8-5V8l-8 5z"/></svg>
          <span>info@brindlewoodgroup.com</span>
        </li>
        <li class="contact__item">
          <svg class="contact__icon" viewBox="0 0 24 24" aria-hidden="true"><path d="M12 3l10 9h-3v9h-5v-6h-4v6H5v-9H2z"/></svg>
          <span>1584 Alder Street,Westbrook,<span class="contact__address-line">MA 02130</span></span>
        </li>
      </ul>
    </section>
  </main>
</body>
</html>
```